cafe brightmill breakfast lunch dinner menu

I am launching my new menu on the 1st of feb and i need a new menu design asap.

This is our logo that we want on the front page

our cafe is industral rustic however we have trees inside everything is timber inside. quite allot of green plants flowers everyhwere.

these photos should give you a understanding of what my cafe looks like and offers
Thanks

Target Market(s)

cafe

Industry/Entity Type

Cafe

Font styles to use
Sans Serif

Colors
85cae6
000000
ffffff
abd036

Requirements
Must have
• 2 pictures of food
Nice to have
• mingloop picvalle logo on the bottom so people can know we are on these platforms.

```html
<!DOCTYPE html>
<html lang="en">
<head>
<meta charset="utf-8">
<title>Cafe Brightmill Menu</title>
<link rel="stylesheet" href="https://fonts.googleapis.com/css2?family=Roboto+Slab:wght@800&family=Indie+Flower&display=swap">
<style>
  :root {
    --board: #383838;
    --board-dark: #2c2c2c;
    --chalk: #ffffff;
    --ink: #111111;
    --photo-breakfast: #7a4a2e;
    --photo-sandwich: #6f6a5c;
    --photo-dessert: #5a4436;
  }
  html, body { margin: 0; padding: 0; overflow: hidden; }
  body { width: 848px; height: 1200px; background: var(--board); }
  .menu {
    position: relative; width: 848px; height: 1200px; overflow: hidden;
    background: radial-gradient(ellipse at 50% 55%, #474747 0%, var(--board) 55%, var(--board-dark) 100%);
    color: var(--chalk);
    font-family: "Indie Flower", cursive;
  }
  .photo-strip { position: absolute; top: 0; left: 0; width: 848px; height: 278px; }
  .photo { position: absolute; top: 0; height: 278px; }
  .photo--breakfast { left: 0; width: 280px; background: linear-gradient(160deg, #a0683f, var(--photo-breakfast) 60%, #3e2a1c); }
  .photo--sandwich { left: 282px; width: 290px; background: linear-gradient(150deg, #8c8578, var(--photo-sandwich) 55%, #46433a); }
  .photo--dessert { left: 574px; width: 274px; background: linear-gradient(170deg, #8a7a6c, var(--photo-dessert) 55%, #2f241d); }
  .divider { position: absolute; left: 428px; top: 302px; width: 4px; height: 786px; background: var(--chalk); }
  .item { position: absolute; width: 400px; text-align: center; }
  .item--left { left: 16px; }
  .item--right { left: 440px; }
  .item-title { position: relative; width: 262px; height: 64px; margin: 0 auto; }
  .item-title svg { position: absolute; inset: 0; width: 100%; height: 100%; }
  .item-title h2 {
    position: relative; margin: 0; line-height: 62px; white-space: nowrap;
    font-family: "Roboto Slab", serif; font-weight: 800; font-size: 21px;
    letter-spacing: -0.4px; color: var(--ink);
  }
  .item-desc { margin: 0; font-size: 19px; line-height: 24px; }
  .item-price { display: block; font-size: 36px; line-height: 42px; font-weight: 700; }
</style>
</head>
<body>
<main class="menu">
  <section class="photo-strip">
    <div class="photo photo--breakfast" role="img" aria-label="Poached eggs with bacon and tomato on toast"></div>
    <div class="photo photo--sandwich" role="img" aria-label="Pastrami sandwich with pickles on a wooden board"></div>
    <div class="photo photo--dessert" role="img" aria-label="Stack of chocolate pancakes with ice cream"></div>
  </section>

  <div class="divider"></div>

  <svg width="0" height="0" style="position:absolute">
    <defs>
      <path id="banner" d="M8 8 L32 2 L62 9 L98 3 L134 8 L174 2 L212 7 L254 3 L248 18 L260 31 L250 43 L258 58 L222 53 L186 62 L146 55 L104 62 L62 54 L26 61 L6 56 L12 43 L2 31 L10 18 Z" fill="#ffffff"/>
    </defs>
  </svg>

  <article class="item item--left" style="top:374px">
    <div class="item-title"><svg viewBox="0 0 262 64"><use href="#banner"/></svg><h2>BACON &amp; Egg Roll</h2></div>
    <p class="item-desc" style="margin-top:12px">orem ipsum dolor sit amet,<br>consectetuer adipiscing elit.<br>Aenean commodo ligula eget<br>dolor. Aenean massa. Cum<br>sociis natoque</p>
    <span class="item-price">$7.50</span>
  </article>

  <article class="item item--left" style="top:636px">
    <div class="item-title"><svg viewBox="0 0 262 64"><use href="#banner"/></svg><h2>BACON &amp; Egg Roll</h2></div>
    <p class="item-desc" style="margin-top:12px">orem ipsum dolor sit amet, consectetuer<br>adipiscing elit.<br>Aenean commodo ligula eget</p>
    <span class="item-price">$3.50</span>
  </article>

  <article class="item item--left" style="top:862px">
    <div class="item-title"><svg viewBox="0 0 262 64"><use href="#banner"/></svg><h2>BACON &amp; Egg Roll</h2></div>
    <p class="item-desc" style="margin-top:24px">Corn Tortillas<br>orem ipsum dolor sit amet,<br>consectetuer adipiscing elit.<br>Aenean commodo ligula eget</p>
    <span class="item-price" style="margin-top:12px;margin-right:38px">$3.50</span>
  </article>

  <article class="item item--right" style="top:370px">
    <div class="item-title"><svg viewBox="0 0 262 64"><use href="#banner"/></svg><h2>BACON &amp; Egg Roll</h2></div>
    <p class="item-desc" style="margin-top:38px">orem ipsum dolor sit amet,<br>consectetuer adipiscing elit.<br>Aenean commodo ligula eget</p>
    <span class="item-price">$6</span>
  </article>

  <article class="item item--right" style="top:636px">
    <div class="item-title"><svg viewBox="0 0 262 64"><use href="#banner"/></svg><h2>BACON &amp; Egg Roll</h2></div>
    <p class="item-desc" style="margin-top:16px">(we love our city)<br>orem ipsum dolor sit amet,<br>consectetuer adipiscing elit.<br>Aenean commodo ligula eget</p>
    <span class="item-price">$6</span>
  </article>

  <article class="item item--right" style="top:862px">
    <div class="item-title"><svg viewBox="0 0 262 64"><use href="#banner"/></svg><h2>BACON &amp; Egg Roll</h2></div>
    <p class="item-desc" style="margin-top:14px">(Kosher &amp; Halal)<br>orem ipsum dolor sit amet,<br>consectetuer adipiscing elit.<br>Aenean commodo ligula eget</p>
    <span class="item-price" style="margin-top:34px;margin-right:38px">$6</span>
  </article>
</main>
</body>
</html>
```